Calendar Infographic Design

I teach and connect Human Resource professionals in the United States. They are almost all women age 35-55. They typically work in small organizations that have less than 100 employees.

We use the attached document as a lead magnet. It is for Human Resources Professionals to keep track of important compliance dates. I'd like it to be more interesting. It can be designed at 8 1/2 X 11 as most people will print it out.

I would like to see more interesting designs that help identify the key deadlines. It should have my branding, but most people know me more than the brand so I am attaching a picture as well for you to consider incorporating - but you do not have to use it.

Target Market(s)

Professional Human Resource Woman Age 55-55

Industry/Entity Type

Human Resources, especially small business

Font styles to use
Sans Serif

Colors
0054AA
0677BA
7BADD7
CADEEF
E8F1F8
FFC000
F8CF3A
FAE287
FDF2CF
FEFAEE
EE7325
F08F49
F5BC92
FAE3D3
FDF4ED

Requirements
Must have
• the dates you see on the current card included and my website www.staffquill.net

```html
<!DOCTYPE html>
<html lang="en">
<head>
<meta charset="utf-8">
<title>Calendar of Critical HR Dates</title>
<link href="https://fonts.googleapis.com/css2?family=Archivo+Black&family=Roboto+Condensed:wght@400;700&family=Source+Sans+3:wght@400;500;600&display=swap" rel="stylesheet">
<style>
  :root{
    --panel:#17498a;
    --ink:#1b3f8b;
    --tab:#fdb913;
    --tab-edge:#f0a20b;
    --accent:#f26b21;
    --card:#ffffff;
    --muted:#555a63;
    --bg-light:#f4f4f5;
    --bg-dark:#dedfe2;
  }
  *{margin:0;padding:0;box-sizing:border-box}
  html,body{width:1200px;height:927px;overflow:hidden}
  body{position:relative;font-family:"Source Sans 3",Arial,sans-serif;background:var(--bg-light)}

  .sidebar{position:absolute;left:0;top:0;width:307px;height:927px;background:var(--panel);color:#fff}
  .brand{position:absolute;left:0;width:307px;top:52px;text-align:center}
  .brand-name{font-family:"Source Sans 3",sans-serif;font-weight:600;font-size:40px;line-height:1;color:#fff;letter-spacing:.5px}
  .brand-tag{font-family:"Roboto Condensed",sans-serif;font-size:10.5px;margin-top:8px;color:#fff}
  .portrait{position:absolute;left:72px;top:146px;width:165px;height:251px;border:3px solid #fff;border-radius:24px;background:linear-gradient(160deg,#8d8f93 0%,#5b82b8 55%,#1f7fc7 100%)}
  .title{position:absolute;left:0;width:307px;top:426px;text-align:center;font-family:"Roboto Condensed",sans-serif;color:#fff;line-height:1}
  .title-top{font-weight:700;font-size:32px}
  .title-bottom{font-weight:400;font-size:32px;margin-top:13px}
  .annual{position:absolute;left:33px;top:628px;width:250px}
  .annual h2{font-family:"Archivo Black",sans-serif;font-weight:400;font-size:29px;color:var(--accent);text-align:center;letter-spacing:.5px;margin-left:-10px}
  .annual ul{list-style:none;margin-top:12px}
  .annual li{position:relative;padding-left:14px;color:var(--accent);font-size:12.6px;font-weight:500;line-height:18.2px}
  .annual li::before{content:"*";position:absolute;left:0;top:0}

  .band{position:absolute;left:307px;width:893px;height:196px}
  .band-1{top:48px;background:linear-gradient(180deg,var(--bg-light),#e9e9eb)}
  .band-2{top:244px;background:linear-gradient(180deg,var(--bg-dark),#f3f3f4)}
  .band-3{top:440px;background:linear-gradient(180deg,var(--bg-dark),#f3f3f4)}
  .band-4{top:636px;background:linear-gradient(180deg,var(--bg-dark),#f3f3f4)}

  .month{position:absolute;width:218px;height:171px;background:var(--card);border-radius:9px}
  .month-tab{position:absolute;left:-8px;top:-7px;width:116px;height:42px;background:var(--tab);border:2px solid var(--tab-edge);border-radius:11px;box-shadow:0 2px 3px rgba(0,0,0,.2);font-family:"Archivo Black",sans-serif;font-size:25px;color:var(--ink);text-align:center;line-height:39px}
  .month ul{position:absolute;left:13px;right:12px;top:60px;list-style:none}
  .month li{position:relative;padding-left:13px;color:var(--ink);font-size:10.9px;font-weight:500;line-height:12.2px;margin-bottom:8.2px;text-align:justify}
  .month li::before{content:"•";position:absolute;left:0;font-size:8px}
  .month sup{font-size:6px;line-height:0}
  .month.dense ul{top:43px}
  .month.dense li{font-size:8.9px;line-height:12.7px;margin-bottom:0}
  .faint-mark{position:absolute;left:0;right:0;top:66px;text-align:center;font-size:30px;font-weight:600;color:#efeff0}

  .col-1{left:409px}.col-2{left:657px}.col-3{left:905px}
  .row-1{top:73px}.row-2{top:269px}.row-3{top:465px}.row-4{top:662px}

  .disclaimer{position:absolute;left:409px;top:861px;font-family:Arial,sans-serif;font-size:10.3px;color:var(--muted);letter-spacing:.1px}
  .copyright{position:absolute;left:409px;top:891px;font-family:Arial,sans-serif;font-size:10.3px;color:var(--muted)}
  .site{position:absolute;right:77px;top:891px;font-family:Arial,sans-serif;font-size:10.3px;color:var(--muted)}
</style>
</head>
<body>
  <aside class="sidebar">
    <div class="brand">
      <div class="brand-name">StaffQuill</div>
      <div class="brand-tag">Compliance Made Simple for Small Teams</div>
    </div>
    <div class="portrait" role="img" aria-label="Portrait photo of the HR consultant in a blue top"></div>
    <h1 class="title"><div class="title-top">CALENDAR OF</div><div class="title-bottom">CRITICAL HR DATES</div></h1>
    <section class="annual">
      <h2>ANNUALLY</h2>
      <ul>
        <li>Review employee handbook for necessary updates</li>
        <li>Determine if your current employment posters are up to date</li>
        <li>Remove all I-9's for terminated employees that are no longer required</li>
        <li>Communicate with employees regarding lack of tolerance for harassment and discrimination</li>
        <li>Complete HR Audit provided as part of Staff Toolkit</li>
      </ul>
    </section>
  </aside>

  <div class="band band-1"></div>
  <div class="band band-2"></div>
  <div class="band band-3"></div>
  <div class="band band-4"></div>

  <section class="month dense col-1 row-1"><div class="month-tab">JAN</div>
    <ul>
      <li>Prepare OSHA 300A</li>
      <li>Gather Data for 5500 reporting; check with broker on requirement</li>
      <li>Advise employees of increase allowed in retirement plan, HSA, dependent care and flexible spending accounts if allowed by law</li>
      <li>Send W2s and 1099s as appropriate</li>
      <li>Be sure to change benefit deductions in payroll</li>
      <li>Download new W4 with current year for new hires</li>
    </ul>
  </section>
  <section class="month col-2 row-1"><div class="month-tab">FEB</div>
    <ul>
      <li>February 1<sup>st</sup> – Post OSHA 300A log</li>
      <li>Consider total compensation statements for previous year</li>
      <li>Black History Month</li>
    </ul>
  </section>
  <section class="month col-3 row-1"><div class="month-tab">MAR</div>
    <ul>
      <li>March 1<sup>st</sup> – Medicare Part D reporting due</li>
      <li>First Friday – National Employee Appreciation day</li>
      <li>EEO-1 (over 100 employees) and VETS 4212 (federal contractors) reports due</li>
    </ul>
  </section>

  <section class="month col-1 row-2"><div class="month-tab">APR</div>
    <ul>
      <li>April 1<sup>st</sup> – H-1B filing begins</li>
      <li>April 30<sup>th</sup> – Take down OSHA 300A and retain for 5 years</li>
    </ul>
  </section>
  <section class="month col-2 row-2"><div class="month-tab">MAY</div><div class="faint-mark">StaffQuill</div></section>
  <section class="month col-3 row-2"><div class="month-tab">JUN</div><div class="faint-mark">StaffQuill</div></section>

  <section class="month col-1 row-3"><div class="month-tab">JUL</div>
    <ul><li>File 5500 for Retirement plan and other benefits if required</li></ul>
  </section>
  <section class="month col-2 row-3"><div class="month-tab">AUG</div>
    <ul><li>Send Summary Plan Description of retirement plan if required</li></ul>
  </section>
  <section class="month col-3 row-3"><div class="month-tab">SEP</div>
    <ul><li>Consider your holiday schedule for payroll and time off and publish to employees</li></ul>
  </section>

  <section class="month col-1 row-4"><div class="month-tab">OCT</div>
    <ul>
      <li>Medicare Part D credible coverage notices to employees</li>
      <li>October 16 – National Boss' Day</li>
    </ul>
  </section>
  <section class="month col-2 row-4"><div class="month-tab">NOV</div>
    <ul>
      <li>Receipt of unemployment rate – verify accuracy</li>
      <li>Remind employees to use FSA dollars</li>
    </ul>
  </section>
  <section class="month col-3 row-4"><div class="month-tab">DEC</div>
    <ul>
      <li>Calculate imputed income for life insurance, personal use of auto, etc.</li>
      <li>Subchapter S corps: Calculate tax implications and reimburse accordingly</li>
    </ul>
  </section>

  <p class="disclaimer">Each organization will have specific deadlines based on size, industry and location.&nbsp; This is not all inclusive or to be taken as legal advice.</p>
  <p class="copyright">©StaffQuill</p>
  <p class="site">www.staffquill.net</p>
</body>
</html>
```